Business Card: RW Office Partners - Your tidy answer finder

Business Name: RW Office Partners
Website: www.rwofficepartners.com.au
Email: marisol@rwofficepartners.com.au
Mobile: 61 487 902 346
Facebook: @rwofficepartners
Instrgram: @rwofficepartners

Brading Colours:
HEX
#986474
#ddccd3
#7a8498
#c9d8e4
#000000
#ffffff

Tag Line: Your Tidy Answer Finder

Link to DRAFT website:
https://helpdeskhub.sitebuilderx.com/rw-office-partners

About Page from the website:
My name is Marisol Bramwell, and I would love to assist you to become more productive in your day to day and achieve your business and personal goals.
My mission is to give you time, time to work on the important tasks of your business or to be able to spend more time with your family. I will take on the tasks you don’t have time for, don’t know well or simply don’t like to do.
I have an extensive background in Administration, Tender Coordination, Document Control, WHS and Quality Management working primarily in the Construction, Mining and Corporate World.
I am passionate about being organised, having order and making things in your life (and mine) easier! I love to watch something unfold and grow into something amazing! I am known for being the go-to problem solver, the organiser of all things, producing high standards of work even under pressure. I’m also a confident communicator, and I understand that you’re busy running your business.

Target Market(s)

Small to Medium Business who require assistance in their business by a virtual assistant.

Industry/Entity Type

Virtual Assistant

Contact Information for Business Card

Mobile: 61 487 902 346

Font styles to use
Sans Serif

Colors
ffffff

Requirements
Must have
• Branding Colours as outlined.
Contact Details as outlined.
Logo as provided.
Proper contact details - mobile, facebook, instragm, website.
Simple, Elegant, very clean looking.
Should not have
• Note cute with pictures.
Not too girly as still want to market to construction companies.

```html
<!DOCTYPE html>
<html lang="en">
<head>
<meta charset="utf-8">
<title>RW Office Partners – Business Card</title>
<link rel="stylesheet" href="https://fonts.googleapis.com/css2?family=Open+Sans:wght@400;500&display=swap">
<style>
  :root {
    --ink: #000000;
    --mauve: #986474;
    --mauve-deep: #784e5a;
    --slate: #7a8498;
    --slate-light: #98a1b5;
    --grey-text: #626268;
  }
  * { margin: 0; padding: 0; box-sizing: border-box; }
  html, body {
    width: 1200px;
    height: 720px;
    overflow: hidden;
    background: var(--ink);
  }
  .card {
    position: relative;
    width: 1200px;
    height: 720px;
    background: var(--ink);
    font-family: "Open Sans", Arial, sans-serif;
    overflow: hidden;
  }
  .brand-square {
    position: absolute;
    left: 108px;
    top: 98px;
    width: 88px;
    height: 88px;
    background: var(--mauve);
  }
  .brand-name {
    position: absolute;
    left: 222px;
    top: 90px;
    color: var(--slate);
    font-weight: 500;
    font-size: 45px;
    line-height: 52px;
    letter-spacing: 2px;
    text-transform: uppercase;
    white-space: nowrap;
  }
  .brand-rule {
    position: absolute;
    left: 108px;
    top: 213px;
    width: 466px;
    height: 3px;
    background: var(--mauve);
  }
  .tagline {
    position: absolute;
    left: 108px;
    top: 226px;
    color: var(--grey-text);
    font-size: 29px;
    font-weight: 400;
    white-space: nowrap;
  }
  .monogram-area {
    position: absolute;
    left: 720px;
    top: 0;
    width: 388px;
    height: 720px;
    background: linear-gradient(160deg, rgba(120, 78, 90, 0.55) 0%, rgba(120, 78, 90, 0.85) 50%, rgba(120, 78, 90, 0.55) 100%);
  }
  .contact-list {
    position: absolute;
    left: 108px;
    top: 341px;
    list-style: none;
  }
  .contact-item {
    display: flex;
    align-items: center;
    height: 57px;
    color: var(--slate-light);
    font-size: 29px;
    white-space: nowrap;
  }
  .contact-icon {
    width: 40px;
    height: 40px;
    flex: none;
    margin-right: 12px;
  }
  .bottom-rule {
    position: absolute;
    left: 0;
    top: 645px;
    width: 1200px;
    height: 4px;
    background: var(--mauve);
    opacity: 0.85;
  }
</style>
</head>
<body>
<main class="card">
  <div class="monogram-area" role="img" aria-label="Large decorative brand monogram"></div>

  <div class="brand-square" aria-hidden="true"></div>
  <div class="brand-name">RW Office<br>Partners</div>
  <div class="brand-rule"></div>
  <p class="tagline">Your Tidy Answer Finder</p>

  <ul class="contact-list">
    <li class="contact-item">
      <svg class="contact-icon" viewBox="0 0 40 40" aria-hidden="true">
        <circle cx="20" cy="20" r="20" fill="var(--mauve)"/>
        <path d="M13.5 11c1-.8 2.1-.6 2.7.4l1.8 3c.5.9.3 1.8-.5 2.4l-1.2.9c.9 2.3 2.7 4.3 5 5.4l1-1.2c.6-.8 1.6-1 2.4-.4l2.9 1.9c.9.6 1.1 1.7.3 2.7l-1.3 1.5c-1 1.1-2.6 1.4-4 .8-5-2-8.8-5.8-10.6-10.8-.5-1.4-.1-2.9 1-3.9z" fill="var(--ink)"/>
      </svg>
      <span>61 487 902 346</span>
    </li>
    <li class="contact-item">
      <svg class="contact-icon" viewBox="0 0 40 40" aria-hidden="true">
        <circle cx="20" cy="20" r="20" fill="var(--mauve)"/>
        <path d="M11 13h18v11H19l-5 4v-4h-3z" fill="none" stroke="var(--ink)" stroke-width="1.8" stroke-linejoin="round"/>
      </svg>
      <span>@rwofficepartners</span>
    </li>
    <li class="contact-item">
      <svg class="contact-icon" viewBox="0 0 40 40" aria-hidden="true">
        <circle cx="20" cy="20" r="20" fill="var(--mauve)"/>
        <g fill="none" stroke="var(--ink)" stroke-width="1.8" stroke-linecap="round">
          <circle cx="20" cy="20" r="3.5"/>
          <path d="M23.5 17v4.5c0 1.8 1 2.8 2.4 2.8 1.6 0 2.6-1.6 2.6-4.3a8.5 8.5 0 1 0-3.4 6.8"/>
        </g>
      </svg>
      <span>@rwofficepartners</span>
    </li>
    <li class="contact-item">
      <svg class="contact-icon" viewBox="0 0 40 40" aria-hidden="true">
        <circle cx="20" cy="20" r="20" fill="var(--mauve)"/>
        <g fill="none" stroke="var(--ink)" stroke-width="1.8">
          <circle cx="20" cy="20" r="9"/>
          <ellipse cx="20" cy="20" rx="4" ry="9"/>
          <line x1="11" y1="20" x2="29" y2="20"/>
          <line x1="12.5" y1="15" x2="27.5" y2="15"/>
          <line x1="12.5" y1="25" x2="27.5" y2="25"/>
        </g>
      </svg>
      <span>www.rwofficepartners.com.au</span>
    </li>
    <li class="contact-item">
      <svg class="contact-icon" viewBox="0 0 40 40" aria-hidden="true">
        <circle cx="20" cy="20" r="20" fill="var(--mauve)"/>
        <g fill="none" stroke="var(--ink)" stroke-width="1.8" stroke-linejoin="round">
          <rect x="11" y="14" width="18" height="12"/>
          <polyline points="11,14 20,21 29,14"/>
          <line x1="11" y1="26" x2="17" y2="19.5"/>
          <line x1="29" y1="26" x2="23" y2="19.5"/>
        </g>
      </svg>
      <span>marisol@rwofficepartners.com.au</span>
    </li>
  </ul>

  <div class="bottom-rule"></div>
</main>
</body>
</html>
```